Communications & Broadcast Consulting/PR/Media Relations & Public Affairs

My main goals are to provide communications support to school districts, small towns/cities/hospitals and private businesses in the form of press releases, media relations, public affairs. I also have 25 years experience as a television news anchor/reporter and I'm open to free-lance reporting in both Indianapolis and other markets. My specialty is working with the media.
Communications

```html
<!DOCTYPE html>
<html lang="en">
<head>
<meta charset="utf-8">
<title>Ridgeline Communications – Business Card</title>
<link href="https://fonts.googleapis.com/css2?family=Lato:wght@300;400;700;900&display=swap" rel="stylesheet">
<style>
  :root {
    --backdrop: #6b6b6b;
    --card-white: #ffffff;
    --band-green: #1f5a2c;
    --card-black: #0b0b0b;
    --accent-lime: #8cc63f;
    --ink: #151515;
    --text-light: #ffffff;
    --tower-grey: #8a8a8a;
  }
  html, body {
    margin: 0;
    padding: 0;
    width: 1200px;
    height: 900px;
    overflow: hidden;
    background: var(--backdrop);
    font-family: "Lato", Arial, sans-serif;
  }
  .canvas {
    position: relative;
    width: 1200px;
    height: 900px;
  }
  .business-card {
    position: absolute;
    left: 100px;
    top: 164px;
    width: 1000px;
    height: 572px;
    border-radius: 34px;
    overflow: hidden;
    background: var(--card-black);
  }
  .card-header {
    height: 200px;
    background: var(--card-white);
    display: flex;
    align-items: flex-end;
    justify-content: center;
    padding-bottom: 40px;
    box-sizing: border-box;
  }
  .company-name {
    margin: 0;
    font-size: 54px;
    font-weight: 400;
    letter-spacing: 0.5px;
    color: var(--ink);
  }
  .name-band {
    height: 100px;
    background: var(--band-green);
    text-align: center;
    color: var(--text-light);
    display: flex;
    flex-direction: column;
    justify-content: center;
  }
  .person-name {
    margin: 0;
    font-size: 42px;
    font-weight: 300;
    line-height: 1.1;
  }
  .person-name .surname { font-weight: 700; }
  .person-title {
    margin: 4px 0 0;
    font-size: 22px;
    font-weight: 700;
  }
  .card-body {
    position: relative;
    height: 272px;
    color: var(--accent-lime);
  }
  .tower-art {
    position: absolute;
    left: 415px;
    top: 10px;
    width: 170px;
    height: 262px;
    border-radius: 6px;
    background: linear-gradient(180deg, rgba(138,138,138,0.55), rgba(138,138,138,0.2));
  }
  .contact-list {
    position: absolute;
    left: 48px;
    top: 118px;
    margin: 0;
    font-size: 25px;
    line-height: 38px;
    display: grid;
    grid-template-columns: auto auto;
    column-gap: 10px;
  }
  .contact-list dt { font-weight: 700; }
  .contact-list dd { margin: 0; }
  .address {
    position: absolute;
    right: 48px;
    top: 118px;
    margin: 0;
    font-style: normal;
    text-align: right;
    font-size: 23px;
    line-height: 36px;
  }
</style>
</head>
<body>
<main class="canvas">
  <article class="business-card">
    <header class="card-header">
      <h1 class="company-name">RIDGELINE COMMUNICATIONS</h1>
    </header>
    <section class="name-band">
      <p class="person-name">Dana <span class="surname">Ridgeway</span></p>
      <p class="person-title">Public &amp; Media Relations Consultant</p>
    </section>
    <section class="card-body">
      <div class="tower-art" role="img" aria-label="Illustration of a broadcast radio tower sending out signal waves"></div>
      <dl class="contact-list">
        <dt>office :</dt><dd>317.555.0142</dd>
        <dt>cell :</dt><dd>317.555.0187</dd>
        <dt>email :</dt><dd>dana@ridgelinecomms.com</dd>
      </dl>
      <address class="address">
        2210 Marlow Court<br>
        Indianapolis, IN 46201
      </address>
    </section>
  </article>
</main>
</body>
</html>
```